Ecommerce Website

Hello designers of Pixel Harbor,

Today I'm requesting webpage designs for my new start up business in Toronto Canada. I have little or no experience in this field so I decided to outsource it here! My business revolves around the retail of customizable smartphone cases, as well as other objects such as mouse pads, mugs, etc.. Our main focus is smartphone cases, tablets and such. There are a few of these types of websites out already so the idea shouldn't be too foreign. I am looking for a minimalist look for my website revolving around light colours. Should convey a sense of simplistic design with elegant feel while including aspects of the business. Please see current website at brindlecove.ca to see how the set-up is (currently on pre-made template). Should have a similar feel to it. Also i have a post for logo design as i currently do not have one. If you can create a logo as well for my other post along with this one, gives preference to artist.

http://jobs.pixelharbor.com/job.aspx?id=587216
Updates

The design should be transferable to the other webpages on the site. The overall look should be the same (borders, buttons, etc)

I am not sure if I'm allowed to request the page in coding as it said non-coded earlier. However it would be preferable to have the website in CSS or HTML as well as a PSD version for alterations.

Wasn't too clear about the total requirements. We are looking for a main homepage as well as a general design for the rest of our pages such as browsing catalogue page, product page, etc.. Should be a general look that can be used for multiple pages.

I have committed the payment so please do not hesitate to post designs.

To All designers.  I have attached the logo to the brief. It has multiple colors which you can choose from. The last one on the second row is the one i prefer the best however if your site can match well with any other ones, that is okay as well. 

Reason: have a few designs for selection in mind however need to get it to the final point.

Target Market(s)

Young adults ages 19 - 32

Industry/Entity Type

Retail

Requirements
Must have
• Main slider design - Main page will have a slider which displays new products or services. Please see brindlecove.ca for example

Note worthy - Currently we are using a service from http://www.vantoriq.com/ so please make sure that it the design will work with that in mind.

```html
<!DOCTYPE html>
<html lang="en">
<head>
<meta charset="utf-8">
<title>Brindle Cove — Home</title>
<link rel="stylesheet" href="https://fonts.googleapis.com/css2?family=Cinzel:wght@400;700&family=Open+Sans:wght@400;600;800&display=swap">
<style>
:root{
  --green:#c3ca55;
  --green-text:#a9b23a;
  --ink:#1e1e1e;
  --grey:#8a8a8a;
  --rule:#d6d6d6;
  --bg:#ffffff;
}
*{box-sizing:border-box;margin:0;padding:0}
html,body{width:882px;height:1200px;overflow:hidden;background:var(--bg)}
body{position:relative;font-family:"Open Sans",Arial,sans-serif;color:var(--ink)}
.abs{position:absolute}

/* brand */
.brand{left:0;width:882px;top:22px;text-align:center}
.brand-dot{width:40px;height:40px;border-radius:50%;background:var(--ink);margin:0 auto 8px}
.brand-name{font-size:13px;letter-spacing:.5px;color:var(--ink)}

/* navigation */
.nav{left:150px;width:563px;top:92px;height:30px;border-left:2px solid var(--ink);border-right:2px solid var(--ink);display:flex;justify-content:center;align-items:center;gap:18px}
.nav a{display:flex;align-items:center;gap:7px;font-size:13px;color:var(--ink);text-decoration:none}
.nav a.is-current{color:var(--green-text)}
.nav svg{width:16px;height:16px;fill:none;stroke:var(--green);stroke-width:1.6}

/* slider */
.slider{left:69px;top:157px;width:742px;height:275px;box-shadow:-4px 8px 10px rgba(0,0,0,.35)}
.slider-photo{height:261px;background:linear-gradient(100deg,#c9b6a8 0%,#eadbd0 30%,#5a5453 48%,#2a2f3a 60%,#e9d2bf 80%,#d6c2b3 100%)}
.slider-band{height:14px;background:var(--green)}

/* section headings */
.section-title{left:0;width:882px;text-align:center;font-family:"Open Sans",Arial,sans-serif;font-weight:800;font-size:22px;letter-spacing:.3px}
.section-sub{left:0;width:882px;text-align:center;font-family:"Cinzel",Georgia,serif;font-size:12px;color:var(--grey);letter-spacing:.5px}
.rule{height:1px;background:var(--rule)}

/* features */
.feature{width:160px;text-align:center}
.feature-disc{width:106px;height:106px;border-radius:50%;background:var(--green);margin:0 auto;display:flex;align-items:center;justify-content:center}
.feature-disc svg{width:54px;height:60px;fill:#fff}
.feature-name{margin-top:26px;font-family:"Cinzel",Georgia,serif;font-size:12px;letter-spacing:.6px}
.feature-note{font-family:"Cinzel",Georgia,serif;font-size:8.5px;color:var(--grey);letter-spacing:.5px}

/* category picker */
.picker{left:645px;top:582px;width:142px}
.picker-title{font-family:"Cinzel",Georgia,serif;font-size:11.5px;font-weight:700}
.picker-sub{font-family:"Cinzel",Georgia,serif;font-size:8.5px;color:#555;letter-spacing:.4px}
.picker-hint{margin-top:10px;font-size:9.5px;color:var(--green-text)}
.picker-select{margin-top:5px;height:30px;border:1px solid #c8c8c8;display:flex;align-items:center;justify-content:center;position:relative;font-size:10px;color:#444}
.picker-select svg{position:absolute;right:10px;top:10px;width:10px;height:8px;fill:none;stroke:#333;stroke-width:1.6}

/* products */
.product{width:200px;text-align:center}
.product-shot{margin:0 auto;border-radius:12px;background:linear-gradient(160deg,#f4f5f6,#c4c8cc 55%,#e8eaec)}
.product-name{margin-top:14px;font-family:"Cinzel",Georgia,serif;font-size:10.5px;line-height:1.2;letter-spacing:.3px}

/* footer */
.foot-col h4{font-family:"Cinzel",Georgia,serif;font-size:9.5px;font-weight:700;letter-spacing:.4px;margin-bottom:8px}
.foot-col li{list-style:none;font-size:7px;color:#555;line-height:15px}
.foot-col p{font-size:6.5px;color:#555;line-height:9px;width:135px}
.branch{display:flex;gap:9px;align-items:flex-start;font-size:6.5px;color:#555;line-height:9px;margin-bottom:9px}
.branch svg{width:11px;height:11px;fill:var(--ink);flex:none}
.legal{left:197px;top:1172px;width:475px;height:28px;background:var(--green);color:#fff;font-size:7px;display:flex;align-items:center;justify-content:center;letter-spacing:.3px}
</style>
</head>
<body>

<header class="brand abs">
  <div class="brand-dot"></div>
  <div class="brand-name">Brindle Cove</div>
</header>

<nav class="nav abs">
  <a class="is-current" href="#"><svg viewBox="0 0 16 16"><path d="M2 8 8 2l6 6M4 7v7h8V7" fill="var(--green)"/></svg>Home</a>
  <a href="#"><svg viewBox="0 0 16 16"><path d="M2 3l12 11"/></svg>Designs</a>
  <a href="#"><svg viewBox="0 0 16 16"><path d="M8 1a5 5 0 0 0-3 9v2h6v-2a5 5 0 0 0-3-9zM6 14h4"/></svg>Create</a>
  <a href="#"><svg viewBox="0 0 16 16"><path d="M8 3c4 0 7 2 7 4.5S12 12 8 12l-4 3 1-3.5C2 11 1 9 1 7.5 1 5 4 3 8 3z"/></svg>About</a>
  <a href="#"><svg viewBox="0 0 16 16"><path d="M1 8 15 2l-3 12-4-4zM8 10v4l2-2M15 2 8 10"/></svg>Contact</a>
  <a href="#"><svg viewBox="0 0 16 16"><path d="M2 9 9 2h5v5l-7 7z"/><circle cx="11.5" cy="4.5" r="1"/></svg>Request a Quote</a>
</nav>

<section class="slider abs">
  <div class="slider-photo" role="img" aria-label="Hands holding a smartphone framing a sunset over a city skyline"></div>
  <div class="slider-band"></div>
</section>

<h2 class="section-title abs" style="top:458px">DESIGN ALL THINGS</h2>
<p class="section-sub abs" style="top:492px">USE YOUR IMAGANATION AS CAN YOU DO, YOU WILL GET</p>
<div class="rule abs" style="left:261px;width:360px;top:530px"></div>

<div class="feature abs" style="left:90px;top:554px">
  <div class="feature-disc"><svg viewBox="0 0 54 60"><path d="M27 4a17 17 0 0 0-10 31c2 2 3 5 3 8h14c0-3 1-6 3-8A17 17 0 0 0 27 4z"/><rect x="20" y="46" width="14" height="3"/><rect x="20" y="51" width="14" height="3"/><rect x="23" y="56" width="8" height="3"/></svg></div>
  <div class="feature-name">HAVE AN IDEA</div>
  <div class="feature-note">SIMPLY MAKE IT</div>
</div>
<div class="feature abs" style="left:268px;top:554px">
  <div class="feature-disc"><svg viewBox="0 0 54 60"><path d="M6 16h12a6 6 0 1 1 10 0h14v12a6 6 0 1 1 0 10v14H28a6 6 0 1 0-10 0H6V38a6 6 0 1 0 0-10z"/></svg></div>
  <div class="feature-name">DESIGN IT</div>
  <div class="feature-note">BY YOUR SELF</div>
</div>
<div class="feature abs" style="left:444px;top:554px">
  <div class="feature-disc" role="img" aria-label="Calligraphic signature flourish"></div>
  <div class="feature-name">MAKE YOUR</div>
  <div class="feature-note">OWN SIGNATURE</div>
</div>

<aside class="picker abs">
  <div class="picker-title">FROM</div>
  <div class="picker-sub">UNLIMATED CATAGORY</div>
  <div class="picker-hint">Select your&nbsp; favorite section</div>
  <div class="picker-select">Mobile<svg viewBox="0 0 10 8"><path d="M1 2l4 4 4-4"/></svg></div>
</aside>

<div class="rule abs" style="left:261px;width:360px;top:750px"></div>
<h2 class="section-title abs" style="top:762px">GET STARTED NOW</h2>
<p class="section-sub abs" style="top:797px">USE YOUR IMAGANATION AS CAN YOU DO, YOU WILL GET</p>
<div class="rule abs" style="left:261px;width:360px;top:839px"></div>

<div class="product abs" style="left:145px;top:880px">
  <div class="product-shot" style="width:150px;height:115px;transform:rotate(-22deg)" role="img" aria-label="Silver touchscreen smartphone"></div>
  <div class="product-name" style="margin-top:22px">Nova Tide S3<br>Decorate from $25 CAD</div>
</div>
<div class="product abs" style="left:342px;top:880px">
  <div class="product-shot" style="width:56px;height:122px" role="img" aria-label="White smartphone front view"></div>
  <div class="product-name">Orbit Four<br>Decorate from $0 CAD</div>
</div>
<div class="product abs" style="left:536px;top:880px">
  <div class="product-shot" style="width:108px;height:110px;margin-top:26px;height:84px;border-radius:8px" role="img" aria-label="Slider phone with keyboard"></div>
  <div class="product-name">Orbit Five<br>Decorate from $0 CAD</div>
</div>

<div class="rule abs" style="left:243px;width:362px;top:1068px"></div>

<div class="foot-col abs" style="left:237px;top:1090px">
  <h4>HOME</h4>
  <ul><li>ABOUT</li><li>SERVICES</li><li>CONTACT US</li></ul>
</div>
<div class="foot-col abs" style="left:347px;top:1090px">
  <h4>MENU</h4>
  <p>benign&nbsp; any useful data, but serves to reserve space enign&nbsp; any useful data, but serves to reserve space where real data is nominally......</p>
</div>
<div class="foot-col abs" style="left:525px;top:1090px">
  <h4>BRANCH</h4>
  <div class="branch"><svg viewBox="0 0 12 12"><path d="M6 0a4 4 0 0 0-4 4c0 3 4 8 4 8s4-5 4-8a4 4 0 0 0-4-4zm0 6a2 2 0 1 1 0-4 2 2 0 0 1 0 4z"/></svg><span>70 Larkfield Row, Halden</span></div>
  <div class="branch"><svg viewBox="0 0 12 12"><path d="M6 0a4 4 0 0 0-4 4c0 3 4 8 4 8s4-5 4-8a4 4 0 0 0-4-4zm0 6a2 2 0 1 1 0-4 2 2 0 0 1 0 4z"/></svg><span>BRANCH2: 145 Quarry Lane,<br>Westmere</span></div>
</div>

<footer class="legal abs">ALLRIGHTS RESEVED @2013</footer>

</body>
</html>
```